Martial Arts & Fitness Center Website

We require a wordpress website for a martial arts and fitness company that is located in Stafford, Texas. The name of the facility is Bright Harbor Martial Arts. This company offers various fitness programs throughout the day, after school care with transportation included, and martial arts programs in the evening. Martial Arts programs in the evening is for beginners, intermediate and advanced students. We web design should be clean, crisp, vibrant, and modern. We also require in addition to the standard pages, at a minimum a contact us page, a registration page for various events at the school (lock-ins, parents night out, after school pickup, etc.) once registered we would like the site to have the option to pay for that service as well. We would like to have the ability to include a shopping cart so we can sell gear on the site.

Target Market(s)

Consumers with school age kids, martial artists, parents with kids in martial arts.

Industry/Entity Type

School

Requirements
Must have
• At least a registration page and contact us page. The ability to add more pages later.

School logo is currently being created and the colors is red, white and blue. Will upload logo as soon as it is received.

```html
<!DOCTYPE html>
<html lang="en">
<head>
<meta charset="utf-8">
<title>Bright Harbor Martial Arts</title>
<link rel="stylesheet" href="https://fonts.googleapis.com/css2?family=Arimo:wght@400;700&family=Roboto+Condensed:wght@400;700&display=swap">
<style>
:root{
  --red:#d20a10;
  --red-dark:#b9060b;
  --red-deep:#a80408;
  --ink:#333;
  --muted:#666;
  --page:#efefef;
  --panel:#fff;
  --line:#e2e2e2;
  --tab:#ececec;
  --gray-btn:#6a6a6a;
}
*{box-sizing:border-box;margin:0;padding:0}
html,body{width:720px;height:1200px;overflow:hidden;background:var(--page);font-family:"Arimo",Arial,sans-serif;color:var(--ink)}
.canvas{position:relative;width:720px;height:1200px;overflow:hidden;background:var(--page)}
.abs{position:absolute}
.topbar{left:0;top:0;width:720px;height:32px;background:var(--red-dark)}
.util-links{right:184px;top:12px;font-size:6px;color:#fff}
.util-links span{margin:0 3px}
.auth{right:26px;top:13px;font-size:7.5px;font-weight:700;color:#fff}
.header{left:0;top:32px;width:720px;height:110px;background:var(--red)}
.brand{left:69px;top:52px;color:#fff}
.brand-name{font-size:22px;font-weight:700;letter-spacing:-0.5px;line-height:1}
.brand-sub{font-size:7.5px;letter-spacing:7.6px;margin-top:5px;white-space:nowrap}
.phones{right:70px;top:38px;color:#fff;font-size:10.5px;font-weight:700}
.phones span{margin-left:16px}
.search{left:468px;top:56px;width:182px;height:18px;background:var(--red-dark);border-radius:2px;color:#f3b3b3;font-size:6px;padding:5px 9px}
.cart{left:551px;top:86px;color:#fff;font-size:6.5px;display:flex;align-items:center;gap:4px}
.cart u{font-weight:700}
.cart small{font-size:4.5px}
.nav{left:74px;top:110px;height:32px;display:flex;font-size:7.5px;color:#fff}
.nav a{padding:0 12px;line-height:32px;color:#fff;text-decoration:none}
.nav a.active{background:var(--red-deep)}
.hero-shadow{left:30px;top:382px;width:660px;height:22px;background:radial-gradient(ellipse at center top,rgba(0,0,0,.28),rgba(0,0,0,0) 70%)}
.hero{left:72px;top:142px;width:576px;height:260px;background:linear-gradient(180deg,#ecedf0 0%,#d8d2cc 45%,#9aa4c2 100%)}
.hero-band{left:72px;top:308px;width:576px;height:64px;background:rgba(190,8,14,.85)}
.hero-title{left:104px;top:316px;color:#fff}
.hero-title .n{font-size:25px;font-weight:700;letter-spacing:-0.6px;line-height:1}
.hero-title .s{font-size:9px;letter-spacing:8.8px;margin-top:3px;white-space:nowrap}
.dots{left:84px;top:384px;display:flex;gap:4px}
.dots i{display:block;width:11px;height:11px;border-radius:50%;background:#fff;border:1px solid #ddd}
.dots i.on{background:var(--red);border:2px solid #fff}
.newsletter-label{left:78px;top:412px;font-family:"Roboto Condensed",Arial,sans-serif;font-size:13px;color:#444}
.newsletter-input{left:316px;top:411px;width:263px;height:19px;background:#e9e9e9;border:1px solid #e0e0e0;font-size:6px;color:#666;padding:5px 9px}
.btn-red{background:var(--red);color:#fff;font-weight:700;text-align:center;border-radius:2px}
.submit{left:585px;top:411px;width:57px;height:19px;font-family:"Roboto Condensed",Arial,sans-serif;font-size:10.5px;line-height:19px}
.content{left:70px;top:446px;width:576px;height:580px;background:var(--panel)}
.side-head{width:144px;height:25px;background:linear-gradient(var(--red),var(--red-dark));color:#fff;font-size:10px;padding:7px 10px;border-radius:2px}
.cat-list{left:78px;top:492px;width:144px;background:#f4f4f4;padding:9px 0 6px;list-style:none}
.cat-list li{font-size:5.8px;color:#555;height:18.7px;line-height:18.7px;padding-left:22px;margin:0 6px;border-bottom:1px dashed #d6d6d6;position:relative;white-space:nowrap}
.cat-list li::before{content:"";position:absolute;left:10px;top:8px;width:4px;height:4px;border-radius:50%;background:#777}
.cat-list li.active{color:var(--red);background:#fff;margin:0;padding-left:28px}
.cat-list li.active::before{background:var(--red);left:16px}
.testimonial{left:84px;width:132px;font-size:6px;line-height:9.3px;color:#555}
.who{left:84px;font-size:7px;font-weight:700;color:#444}
.crumb{left:248px;top:464px;font-size:7px;color:#444}
.crumb b{color:var(--red);font-weight:400}
.tabs{left:246px;top:478px;width:396px;height:24px;background:var(--tab);display:flex;font-size:7px;color:#555;padding-left:25px}
.tabs span{line-height:24px;margin-right:30px;white-space:nowrap}
.tabs span.on{color:var(--red);text-decoration:underline}
.card{width:160px;height:70px;background:#f7f7f7;border:1px solid #ebebeb}
.thumb{position:absolute;left:5px;top:14px;width:50px;height:46px;background:#fff;border:1px solid #e4e4e4}
.card .title{position:absolute;left:62px;top:11px;font-size:6.6px;color:#444;white-space:nowrap}
.card .price{position:absolute;left:62px;top:24px;font-size:17px;font-weight:700;color:#333}
.card .buy,.card .add{position:absolute;top:51px;width:42px;height:10px;font-size:5px;line-height:10px;color:#fff;text-align:center;border-radius:2px}
.card .buy{left:64px;background:var(--gray-btn)}
.card .add{left:110px;background:var(--red)}
.pager{left:280px;top:756px;width:326px;height:20px;background:#f0f0f0;font-size:7px;color:#666;padding:0 16px;line-height:20px}
.pager .pages span{margin-right:15px}
.pager .pages span:first-child{color:var(--red)}
.pager .nav-r{position:absolute;right:8px;top:0;font-weight:700}
.section-title{font-size:10px;color:var(--red);white-space:nowrap}
.about-photo{left:280px;top:824px;width:108px;height:72px;background:linear-gradient(180deg,#c9b79f,#e8e4df 60%,#f1ede9)}
.about-text{left:396px;top:822px;width:246px;font-size:6.1px;line-height:9.3px;color:#555;text-align:justify}
.read-more{left:585px;top:881px;width:57px;height:17px;font-size:7px;line-height:17px}
.featured-item{top:938px;height:52px;background:#f2f2f2}
.arrow{top:948px;font-size:22px;color:#777;line-height:1}
.footer{left:0;top:1026px;width:720px;height:174px;background:var(--red)}
.fcol{top:1043px;color:#fff;font-size:6px;list-style:none;white-space:nowrap}
.fcol li{height:16.1px}
.sitemap-title{left:417px;top:1041px;color:#fff;font-family:"Roboto Condensed",Arial,sans-serif;font-size:11px;font-weight:700}
.map{left:418px;top:1060px;width:232px;height:94px;background:linear-gradient(135deg,#d8e2e6,#ece8de 55%,#d4e2ea)}
.social{top:1170px;width:20px;height:19px;background:#2aa2d8;border-radius:2px}
.social.b{background:#39609e}
.pay{top:1170px;width:36px;height:19px;background:#fff;border-radius:2px}
.copy{left:76px;top:1178px;font-size:5.5px;color:#fff}
</style>
</head>
<body>
<div class="canvas">

  <div class="abs topbar"></div>
  <div class="abs util-links"><span>Check Out</span>|<span>Order Status</span>|<span>Wish List</span>|<span>Help</span>|<span>Account</span></div>
  <div class="abs auth">LOGIN &nbsp;| &nbsp;REGISTER</div>

  <header class="abs header"></header>
  <div class="abs brand"><div class="brand-name">Bright Harbor</div><div class="brand-sub">MARTIAL ARTS</div></div>
  <div class="abs phones">PHONE : 1-555-210-4411<span>TOLL FREE : &nbsp;(800) 555-0192</span></div>
  <div class="abs search">Search
    <svg class="abs" style="right:8px;top:4px" width="10" height="10" viewBox="0 0 10 10"><circle cx="4" cy="4" r="3" fill="none" stroke="#e07a7a" stroke-width="1.2"/><line x1="6.2" y1="6.2" x2="9" y2="9" stroke="#e07a7a" stroke-width="1.2"/></svg>
  </div>
  <div class="abs cart">
    <svg width="15" height="12" viewBox="0 0 15 12"><path d="M1 1h2.5l1.6 7h7.4l1.5-5H4.2" fill="none" stroke="#fff" stroke-width="1.1"/><circle cx="6" cy="10.5" r="1" fill="#fff"/><circle cx="11.5" cy="10.5" r="1" fill="#fff"/></svg>
    <u>View Cart</u><small>(Your Cart is empty)</small>
  </div>
  <nav class="abs nav">
    <a class="active">HOME</a><a>COURSES</a><a>LOCK-INS</a><a>PARENTS</a><a>NIGHTOUT</a><a>SCHOOL PICKUP</a><a>REGISTER</a><a>CONTACT US</a>
  </nav>

  <div class="abs hero-shadow"></div>
  <div class="abs hero" role="img" aria-label="Photo of children in white uniforms practising kicks with an instructor in a training hall"></div>
  <div class="abs hero-band"></div>
  <div class="abs hero-title"><div class="n">Bright Harbor</div><div class="s">MARTIAL ARTS</div></div>
  <div class="abs dots"><i class="on"></i><i></i><i></i><i></i></div>

  <div class="abs newsletter-label">Free &nbsp;Newsletter Updates to your E-mail ID</div>
  <div class="abs newsletter-input">Enter your e- mail address</div>
  <div class="abs btn-red submit">SUBMIT</div>

  <main class="abs content"></main>

  <div class="abs side-head" style="left:78px;top:464px">Shop by category</div>
  <ul class="abs cat-list">
    <li>ACCESSORIES</li><li>APPAREL</li><li class="active">BELTS</li><li>BOXING</li><li>FITNESS STRETCHING</li><li>GLOVES</li><li>MARTIAL ARTS WEAPONS</li><li>MIXED MARTIAL ARTS</li><li>TRAINING DVDS</li><li>PATCH &amp; ACHIEVEMENT</li><li>SPARRING GEAR</li><li>TARGETS &amp; SHIELDS</li><li>TRAINING BAGS</li><li>UNIFORMS</li>
  </ul>

  <div class="abs side-head" style="left:78px;top:773px">Testimonials</div>
  <p class="abs testimonial" style="top:814px">“ Mainly because martial arts seem to be more than just a sport. Football is fine for its fitness and teamwork, but doesn't give the personal development and discipline that martial arts can provide.”</p>
  <div class="abs who" style="top:871px">Dale,Texas</div>
  <p class="abs testimonial" style="top:887px">“ Mainly because martial arts seem to be more than just a sport. Football is fine for its fitness and teamwork, but doesn't give the personal development and discipline that martial arts can provide.”</p>
  <div class="abs who" style="top:944px">Rosa,Texas</div>

  <div class="abs crumb">Home &gt; Belts &gt; <b>Solid</b></div>
  <div class="abs tabs"><span class="on">Solid</span><span>Stripe</span><span>Single Wrap</span><span>Double wrap</span><span>Adjustable</span><span>Balck Belt</span></div>

  <div class="abs card" style="left:280px;top:514px"><div class="thumb" role="img" aria-label="Belt colour swatches" style="background:linear-gradient(180deg,#e8a53a 0 18%,#fff 18% 30%,#5b5f6b 30%,#c04a3a 60%,#3f6e8f 100%)"></div><div class="title">Double Wrap Soild Belt</div><div class="price">$10.00</div><div class="buy">Buy Now</div><div class="add">Add Cart</div></div>
  <div class="abs card" style="left:446px;top:514px"><div class="thumb" role="img" aria-label="Belt colour swatches" style="background:linear-gradient(180deg,#e8a53a 0 18%,#fff 18% 30%,#5b5f6b 30%,#c04a3a 60%,#3f6e8f 100%)"></div><div class="title">Single &nbsp;Wrap Soild Belt</div><div class="price">$10.00</div><div class="buy">Buy Now</div><div class="add">Add Cart</div></div>
  <div class="abs card" style="left:280px;top:596px"><div class="thumb" role="img" aria-label="Adjustable belt colour swatches" style="background:linear-gradient(180deg,#e45a2a 0 16%,#fff 16% 28%,#d94a2a 28%,#e8b24a 60%,#2f5f8f 100%)"></div><div class="title">Adjustable Soild Belt</div><div class="price">$10.00</div><div class="buy">Buy Now</div><div class="add">Add Cart</div></div>
  <div class="abs card" style="left:446px;top:596px"><div class="thumb" role="img" aria-label="Stack of coloured no-tie belts" style="background:linear-gradient(180deg,#1f2a3a 0 22%,#fff 22% 30%,#2d7a3a 30% 50%,#c8362c 50% 72%,#e8cc3a 72%)"></div><div class="title">No Tie Belt</div><div class="price">$10.00</div><div class="buy">Buy Now</div><div class="add">Add Cart</div></div>
  <div class="abs card" style="left:280px;top:678px"><div class="thumb" role="img" aria-label="Striped belts" style="background:linear-gradient(180deg,#f0f0f0 0 20%,#b8322c 20% 38%,#f0f0f0 38% 60%,#f1f1f1 60% 78%,#2f7ad0 78%)"></div><div class="title">Solid Belt Stripes</div><div class="price">$10.00</div><div class="buy">Buy Now</div><div class="add">Add Cart</div></div>
  <div class="abs card" style="left:446px;top:678px"><div class="thumb" role="img" aria-label="Black belt" style="background:linear-gradient(180deg,#fff 0 18%,#141a18 18% 88%,#fff 88%)"></div><div class="title">Deluxe Black Belt</div><div class="price">$10.00</div><div class="buy">Buy Now</div><div class="add">Add Cart</div></div>

  <div class="abs pager"><span class="pages"><span>1</span><span>2</span><span>3</span><span>4</span></span><span class="nav-r">Prev | Next</span></div>

  <div class="abs section-title" style="left:280px;top:802px">About Bright Harbor Martial arts</div>
  <div class="abs about-photo" role="img" aria-label="Group photo of students and instructors in uniforms"></div>
  <p class="abs about-text">Contrary to popular belief, Lorem Ipsum is not simply random text. It has roots in a piece of classical Latin literature from 45 BC, making it over 2000 years old. A Latin professor at a college in Virginia, looked up one of the more obscure Latin words, consectetur, from a Lorem Ipsum passage, and going through the cites of the word in classical literature, discovered the undoubtable source.</p>
  <div class="abs btn-red read-more">Read More</div>

  <div class="abs section-title" style="left:280px;top:912px">Featured Products</div>
  <div class="abs arrow" style="left:282px">‹</div>
  <div class="abs featured-item" role="img" aria-label="Sparring helmet and gear" style="left:307px;width:51px;background:linear-gradient(135deg,#f4f4f4,#3a5a9a 50%,#f4f4f4)"></div>
  <div class="abs featured-item" role="img" aria-label="Black gear bag" style="left:364px;width:78px;background:linear-gradient(180deg,#ececec,#222 40%,#333 80%,#ececec)"></div>
  <div class="abs featured-item" role="img" aria-label="Black uniform" style="left:456px;width:53px;background:linear-gradient(180deg,#f4f4f4,#1b1b1b 25%,#1b1b1b 90%,#f4f4f4)"></div>
  <div class="abs featured-item" role="img" aria-label="Rolled coloured belts" style="left:518px;width:80px;background:linear-gradient(90deg,#e8a030,#d8402a,#3a6ac8,#3a9a4a,#e8d040)"></div>
  <div class="abs arrow" style="left:620px">›</div>

  <footer class="abs footer"></footer>
  <ul class="abs fcol" style="left:78px"><li>HOME</li><li>COURSES</li><li>LOCK-INS</li><li>SCHOOL PICKUP</li><li>REGISTER</li><li>CONTACT US</li></ul>
  <ul class="abs fcol" style="left:150px"><li>MARTIAL ARTS SHOP</li><li>CONTACT US</li><li>EDIT YOUR ACCOUNT</li><li>KIDS DISCOUNTS</li><li>SHOPPING CART</li><li>TERMS AND CONDITIONS</li></ul>
  <ul class="abs fcol" style="left:245px"><li>KIDS MARTIAL ARTS</li><li>COMPETITIONS</li><li>EVENTS</li><li>TODAY</li><li>MARTIAL ARTS NEWS</li></ul>
  <ul class="abs fcol" style="left:320px"><li>ACCESSORIES</li><li>APPAREL</li><li>BOXING</li><li>FITNESS STRETCHING</li><li>GLOVES</li><li>MARTIAL ARTS WEAPONS</li><li>MIXED MARTIAL ARTS</li></ul>
  <svg class="abs" style="left:345px;top:1155px" width="8" height="6" viewBox="0 0 8 6"><path d="M1 1l3 3 3-3" fill="none" stroke="#fff" stroke-width="1.3"/></svg>

  <div class="abs sitemap-title">SITEMAP LOCATION</div>
  <div class="abs map" role="img" aria-label="Map showing the school location"></div>

  <div class="abs social" style="left:416px"></div>
  <div class="abs social b" style="left:443px"></div>
  <div class="abs social b" style="left:469px"></div>
  <div class="abs pay" style="left:498px"></div>
  <div class="abs pay" style="left:537px"></div>
  <div class="abs pay" style="left:576px"></div>
  <div class="abs pay" style="left:615px;width:34px"></div>

  <div class="abs copy">© Copyright 2011-2012 bright harbor martial arts, All rights reserved</div>
</div>
</body>
</html>
```